Need a simple buisness card for my plumbing business. Would like it to be black background with white text.

Industry/Entity Type

Business

Requirements
Must have
• On the front of the card I need to have,
TKW PLUMBING SERVICES
PLUMBERS, DRAINERS & GASFITTERS
Dorian Lessop
0491576038
Info@tkwplumbingservices.com.au
LIC No 518047k
ABN No 57091836254
On the back I need in point form
Domestic,industrial,commercial, all new installations, renovations, sewer renewals, repairs,
Fully licensed and insured
Nice to have
• A nice simple logo

```html
<!DOCTYPE html>
<html lang="en">
<head>
<meta charset="utf-8">
<title>TKW Plumbing Services — Business Card</title>
<link rel="stylesheet" href="https://fonts.googleapis.com/css2?family=Arimo:wght@400;700&family=Roboto:wght@300&display=swap">
<style>
  :root {
    --stage: #8c8c8c;
    --stage-light: #a6a6a6;
    --card-dark: #050505;
    --card-mid: #262626;
    --silver: #d9d9d9;
    --silver-dark: #8a8a8a;
    --white: #f4f4f4;
  }
  * { margin: 0; padding: 0; box-sizing: border-box; }
  html, body { width: 1200px; height: 1200px; overflow: hidden; }
  body {
    background: radial-gradient(circle at 50% 50%, var(--stage-light), var(--stage));
    font-family: "Arimo", Arial, sans-serif;
    position: relative;
  }
  .card {
    position: absolute;
    left: 206px;
    width: 760px;
    height: 452px;
    background: radial-gradient(ellipse at 55% 60%, var(--card-mid) 0%, #141414 45%, var(--card-dark) 100%);
    box-shadow: 0 18px 40px rgba(0,0,0,0.55);
    overflow: hidden;
  }
  .card--front { top: 89px; }
  .card--back { top: 616px; }
  .silver {
    position: absolute;
    white-space: nowrap;
    font-weight: 700;
    text-transform: uppercase;
    background: linear-gradient(180deg, var(--white) 0%, var(--silver) 45%, var(--silver-dark) 100%);
    -webkit-background-clip: text;
    background-clip: text;
    color: transparent;
    filter: drop-shadow(1px 2px 1px rgba(0,0,0,0.9));
  }
  .tool-mark {
    position: absolute;
    left: 394px;
    top: 19px;
    width: 324px;
    height: 324px;
  }
  .brand-name {
    position: absolute;
    left: 28px;
    top: -14px;
    font-family: "Roboto", Arial, sans-serif;
    font-weight: 300;
    font-size: 134px;
    letter-spacing: 2px;
    color: var(--silver);
    line-height: 1;
  }
  .trade-name { left: 88px; top: 104px; font-size: 27px; }
  .trade-name small { font-size: 21px; }
  .trade-lines { left: 151px; top: 134px; font-size: 14px; letter-spacing: 0.5px; }
  .contact-name { left: 52px; top: 212px; font-size: 19px; }
  .contact-phone { left: 361px; top: 212px; font-size: 19px; letter-spacing: 1px; }
  .contact-email { left: 52px; top: 246px; font-size: 19px; text-transform: none; font-weight: 400; }
  .registration { left: 304px; top: 406px; font-size: 14px; word-spacing: 3px; }
  .service { font-size: 16px; }
  .assurance { left: 118px; top: 362px; font-size: 24px; }
</style>
</head>
<body>
  <section class="card card--front">
    <svg class="tool-mark" role="img" aria-label="Faint crossed wrench and pliers decoration" viewBox="0 0 324 324">
      <defs>
        <radialGradient id="toolGlow" cx="50%" cy="50%" r="50%">
          <stop offset="0%" stop-color="#000" stop-opacity="0.55"/>
          <stop offset="100%" stop-color="#000" stop-opacity="0"/>
        </radialGradient>
      </defs>
      <rect width="324" height="324" fill="url(#toolGlow)"/>
    </svg>
    <div class="brand-name">TKW</div>
    <div class="silver trade-name">Plumbing <small>Services</small></div>
    <div class="silver trade-lines">Plumbers, Drainers &amp; Gasfitters</div>
    <div class="silver contact-name">Dorian Lessop</div>
    <div class="silver contact-phone">0491576038</div>
    <div class="silver contact-email">Info@tkwplumbingservices.com.au</div>
    <div class="silver registration">ABN Nº 57091836254 &nbsp;LIC Nº 518047K</div>
  </section>

  <section class="card card--back">
    <ul class="service-list">
      <li class="silver service" style="left:124px;top:92px">Domestic</li>
      <li class="silver service" style="left:180px;top:116px">Industrial</li>
      <li class="silver service" style="left:233px;top:138px">Commercial</li>
      <li class="silver service" style="left:298px;top:161px">All New Renovations</li>
      <li class="silver service" style="left:361px;top:180px">Renovations</li>
      <li class="silver service" style="left:415px;top:202px">Sewer Renewals</li>
      <li class="silver service" style="left:473px;top:221px">Repairs</li>
    </ul>
    <div class="silver assurance">Fully Licensed and Insured</div>
  </section>
</body>
</html>
```